Web Design Project

Tern Ballast needs a new web page design.

This final product MUST be a layered .psd format for our CSS coder to do properly.

What we need is a 3 column template similar to the attached sample. We NEED to have 3 defined sections "Learn" "Shop" and "Dive." This is very important.

Our store font is Ethnocentric, so any design which incorporates this somehow would be great. Our logo is attached in a .jpeg and .psd format. Feel free to manipulate the logo background into a design that works.

Preferred colors are blue (not light blue,) grey, black and yellow. The center section of the template must remain white.

Tern Ballast is a website for technical and rebreather equipment, and training. PLEASE do NOT show images of recreational scuba divers. This is not our market and designs featuring recreational 'touristy' divers will be eliminated.

Attached are logos, and images for use as a background image.

Target Market(s)

Males 25-60

Industry/Entity Type

Store

Requirements
Must have
• - 3 defined sections "Learn" "Shop" "Dive"
- White center area
- Final format must be delivered in a layered .psd file for our CSS coder to cut
Nice to have
• -Ethnocentric fonts
-3d borders
-Textures
- Blue, great black, yellow colors.
- Simple, uncluttered design
Should not have
• Images or logos of recreational or 'tourist' scuba divers. This is a technical and rebreather diving business.

Light blue colors

```html
<!DOCTYPE html>
<html lang="en">
<head>
<meta charset="utf-8">
<title>Tern Ballast Store</title>
<link href="https://fonts.googleapis.com/css2?family=Orbitron:wght@700;900&family=Arimo:ital,wght@0,400;0,700;1,700&display=swap" rel="stylesheet">
<style>
:root{
  --ocean-top:#0d4f8f;
  --ocean-mid:#0a3566;
  --abyss:#000000;
  --navy:#0b1f5c;
  --link:#0c2a6b;
  --yellow:#ffd200;
  --ice:#a9ecff;
  --white:#ffffff;
  --grey:#c9c9c9;
  --rule:#d4d4d4;
  --ink:#222222;
}
*{box-sizing:border-box;margin:0;padding:0}
html,body{width:1200px;height:1019px;overflow:hidden}
body{position:relative;font-family:"Arimo",Arial,sans-serif;color:var(--ink);
  background:linear-gradient(180deg,var(--ocean-top) 0%,var(--ocean-mid) 35%,#06203f 62%,var(--abyss) 85%)}
.abs{position:absolute}
a{text-decoration:none;color:inherit}

/* top nav */
.top-nav{left:543px;top:0;width:440px;height:34px;background:linear-gradient(180deg,#0a2340,#06152a);
  border-radius:0 0 0 12px;display:flex;align-items:center;font:700 11px "Arimo",sans-serif;color:var(--white)}
.top-nav .sep{margin:0 20px}
.top-nav .first{margin-left:30px}
.view-cart{left:980px;top:0;width:130px;height:34px;background:linear-gradient(180deg,#2d8fb0,#17617f);
  border-radius:0 0 12px 0;display:flex;align-items:center;gap:6px;padding-left:10px;
  font:700 12px "Arimo",sans-serif;color:var(--yellow)}

/* brand */
.brand{left:126px;top:100px;display:flex;align-items:center;gap:10px}
.brand .dot{width:16px;height:16px;border-radius:50%;background:var(--white)}
.brand .name{font:700 32px "Arimo",sans-serif;color:var(--white);letter-spacing:1px}

/* contact + search */
.call{left:515px;top:72px;font:italic 700 12px "Arimo",sans-serif;color:var(--yellow)}
.phone{left:639px;top:59px;font:italic 700 27px "Arimo",sans-serif;color:var(--white)}
.search{left:507px;top:91px;width:304px;height:24px;border-radius:12px;overflow:hidden;display:flex;
  box-shadow:0 1px 2px rgba(0,0,0,.5)}
.search .field{flex:1;background:linear-gradient(180deg,#e6e6e6,#b9b9b9)}
.search .go{width:103px;background:linear-gradient(180deg,#1d5a96,#0a2d5a);font:700 13px "Arimo",sans-serif;
  color:var(--yellow);display:flex;align-items:center;justify-content:center}
.free{left:879px;top:66px;font:italic 700 27px "Arimo",sans-serif;color:var(--ice);letter-spacing:-.5px}
.free-sub{left:941px;top:102px;font:700 13px "Arimo",sans-serif;color:var(--yellow)}

/* tab strip */
.intl{left:375px;top:155px;width:300px;height:34px;background:linear-gradient(90deg,rgba(6,21,42,0),#06152a 20%);
  display:flex;align-items:center;padding-left:5px;font:13px "Arimo",sans-serif;color:var(--white)}
.intl b{color:var(--yellow);font-size:11px;margin-left:10px}
.tabs{left:668px;top:145px;width:442px;height:44px;background:linear-gradient(180deg,#1f6fa3,#0f4d7c);
  clip-path:polygon(14px 0,100% 0,100% 100%,0 100%);display:flex;align-items:center;
  font:700 16px "Arimo",sans-serif;color:var(--white);padding-top:8px}
.tabs span{display:flex;align-items:center;justify-content:center;height:26px}
.tabs .best{width:164px;color:var(--yellow);border-right:1px solid #cfe6f5}
.tabs .new{width:166px;border-right:1px solid #cfe6f5}
.tabs .sale{width:100px}

/* main panel */
.panel{left:89px;top:189px;width:1021px;height:732px;background:var(--white);border-radius:14px}
.section-head{top:218px;height:36px;border:1px dashed #333;border-radius:8px;display:flex;align-items:center;justify-content:center;
  font:900 19px "Orbitron",sans-serif;letter-spacing:1px;color:#000}
.head-learn{left:98px;width:242px;padding-right:14px}
.head-shop{left:371px;width:462px}
.head-dive{left:864px;width:240px;padding-left:22px}
.badge{width:50px;height:50px;border-radius:50%;background:var(--navy);border:4px solid #1a5fb0;top:210px}
.col-rule{top:262px;width:1px;height:622px;background:var(--rule)}

/* learn */
.learn-title{width:230px;text-align:center;font:400 14px "Arimo",sans-serif;color:var(--navy)}
.photo{background:linear-gradient(135deg,#b9a48e,#6e6258 55%,#d6d2c8)}
.blurb{font:11px/16px "Arimo",sans-serif;color:var(--ink);width:200px}
.more{font:11px "Arimo",sans-serif;color:var(--link)}

/* shop */
.tile{width:158px;height:142px;border:1px solid var(--grey);background:var(--white);display:flex;align-items:center;justify-content:center}
.tile i{display:block;width:110px;height:118px;border-radius:10px}
.label{width:158px;text-align:center;font:12px "Arimo",sans-serif;color:#111}

/* dive */
.event{left:884px;width:215px}
.event h3{font:400 14px "Arimo",sans-serif;color:var(--navy)}
.event .date{font:12px "Arimo",sans-serif;color:#111;margin-top:3px}
.event p{font:11px/16px "Arimo",sans-serif;color:var(--ink);margin-top:10px;padding-left:2px;width:192px}
.event .more{display:block;text-align:right;margin-top:10px;padding-right:4px}

.footer{left:726px;top:943px;font:11px "Arimo",sans-serif;color:var(--white)}
.footer .sep{margin:0 10px}
</style>
</head>
<body>

<nav class="abs top-nav">
  <a class="first" href="#">HOME</a><span class="sep">|</span>
  <a href="#">ABOUT US</a><span class="sep">|</span>
  <a href="#">SEND EMAIL</a><span class="sep">|</span>
  <a href="#">PRIVACY POLICY</a>
</nav>
<a class="abs view-cart" href="#">
  <svg width="34" height="24" viewBox="0 0 34 24" fill="none" stroke="#e8eef2" stroke-width="2">
    <path d="M2 3h6l4 13h15l4-10H10"/><circle cx="14" cy="20" r="2"/><circle cx="26" cy="20" r="2"/>
  </svg>VIEW CART
</a>

<div class="abs brand"><span class="dot"></span><span class="name">TERN BALLAST</span></div>

<div class="abs call">Questions ? Call us!</div>
<div class="abs phone">239.555.0147</div>
<div class="abs search"><span class="field"></span><span class="go">SEARCH</span></div>
<div class="abs free">FREE SHIPPING!</div>
<div class="abs free-sub">In the Continental U.S. &#9654;</div>

<div class="abs intl">Shipppping International ? <b>CLICK FOR DETAILS</b></div>
<div class="abs tabs"><span class="best">BEST SELLERS</span><span class="new">NEW ARRIVALS</span><span class="sale">SALE</span></div>

<main class="abs panel"></main>

<div class="abs section-head head-learn">LEARN</div>
<div class="abs section-head head-shop">SHOP</div>
<div class="abs section-head head-dive">DIVE</div>
<span class="abs badge" style="left:312px"></span>
<span class="abs badge" style="left:839px"></span>
<span class="abs col-rule" style="left:338px"></span>
<span class="abs col-rule" style="left:863px"></span>

<!-- learn column -->
<h2 class="abs learn-title" style="left:98px;top:276px">Sanitab disinfectant</h2>
<div class="abs photo" role="img" aria-label="Presenter holding a disinfectant bottle in a workshop" style="left:113px;top:301px;width:200px;height:127px"></div>
<p class="abs blurb" style="left:115px;top:433px">If you haven't installed your new software, begin by reading some infor-mation on installation and other prelimi-</p>
<a class="abs more" href="#" style="left:256px;top:494px">Watch Video</a>

<h2 class="abs learn-title" style="left:98px;top:538px">Ready to pick your rebreather?</h2>
<div class="abs photo" role="img" aria-label="Instructor seated with a rebreather unit in a dive shop" style="left:114px;top:563px;width:200px;height:133px"></div>
<p class="abs blurb" style="left:115px;top:707px">If you haven't installed your new software, begin by reading some infor-mation on installation and other prelimi-</p>
<a class="abs more" href="#" style="left:256px;top:768px">Watch Video</a>

<!-- shop grid -->
<div class="abs tile" style="left:353px;top:286px"><i role="img" aria-label="Black backplate and wing" style="background:linear-gradient(180deg,#444,#111)"></i></div>
<div class="abs tile" style="left:523px;top:286px"><i role="img" aria-label="Wrist dive computer and transmitter" style="background:linear-gradient(180deg,#555,#1a1a1a)"></i></div>
<div class="abs tile" style="left:692px;top:286px"><i role="img" aria-label="Exposure suit with harness" style="background:linear-gradient(180deg,#2a2a2a,#1b3fa0)"></i></div>
<div class="abs label" style="left:353px;top:436px">Back Plates/Wings</div>
<div class="abs label" style="left:523px;top:438px">Electronics</div>
<div class="abs label" style="left:692px;top:436px">Exposure Protection</div>

<div class="abs tile" style="left:353px;top:478px"><i role="img" aria-label="Yellow dive tanks" style="background:linear-gradient(180deg,#f2f25a,#b8c400)"></i></div>
<div class="abs tile" style="left:523px;top:478px"><i role="img" aria-label="Steel tank bands" style="background:linear-gradient(180deg,#eee,#888 60%,#ddd)"></i></div>
<div class="abs tile" style="left:692px;top:478px"><i role="img" aria-label="Dive torch" style="background:linear-gradient(160deg,#fff,#666 50%,#fff)"></i></div>
<div class="abs label" style="left:353px;top:626px">Tanks</div>
<div class="abs label" style="left:523px;top:628px">Hardware</div>
<div class="abs label" style="left:692px;top:626px">Lights</div>

<div class="abs tile" style="left:353px;top:663px"><i role="img" aria-label="Rebreather harness" style="background:linear-gradient(180deg,#555,#1a1a1a)"></i></div>
<div class="abs tile" style="left:523px;top:663px"><i role="img" aria-label="Regulator first and second stage" style="background:linear-gradient(160deg,#333,#2d5fb0 60%,#bbb)"></i></div>
<div class="abs tile" style="left:692px;top:663px"><i role="img" aria-label="Dive fin" style="background:linear-gradient(180deg,#222,#b0201a)"></i></div>
<div class="abs label" style="left:353px;top:816px">Rebreathers</div>
<div class="abs label" style="left:523px;top:818px">Regulators</div>
<div class="abs label" style="left:692px;top:816px">Fins</div>
<a class="abs more" href="#" style="left:808px;top:856px;font-size:12px">View All</a>

<!-- dive column -->
<article class="abs event" style="top:276px">
  <h3>Deepwater Expo 2012!</h3><div class="date">May 20 to June 02</div>
  <p>If you haven't installed your new software, begin by reading some infor-mation on installation and other prelimi-</p>
  <a class="more" href="#">Read More</a>
</article>
<article class="abs event" style="top:426px">
  <h3>Truck Lagoon CCR Trip</h3><div class="date">May 20 to June 02</div>
  <p>If you haven't installed your new software, begin by reading some infor-mation on installation and other prelimi-</p>
  <a class="more" href="#">Read More</a>
</article>
<article class="abs event" style="top:582px">
  <h3>Dive with team Tern Ballast</h3><div class="date">May 20 to June 02</div>
  <p>If you haven't installed your new software, begin by reading some infor-mation on installation and other prelimi-</p>
  <a class="more" href="#">Read More</a>
</article>

<footer class="abs footer">Copyright &copy; 2012 Tern Ballast.&nbsp;&nbsp; All rights reserved<span class="sep">|</span>Terms and Conditions</footer>

</body>
</html>
```